Verpackungen für Display Schutzglas
Vielen Dank für die tolle Zusammenarbeit, vom Anfang bis zum Ende war es uns eine Freude die Verpackung bzw. das Design zusammen zu gestalten.
Zielgruppe
Wir verkaufen Smartphone und Tabletzubehör. Für unseren Shop (Ladengeschäft) brauchen wir eine Verpackung für unser Display Schutzglas.
Aufgabenstellung
Wir möchten eine Verpackung die auf der Vorderseite sehr einfach gestaltet ist. Hier bitte nur auf das wesentliche hinweisen. Auf der Rückseite alles weitere wie Installation und Inhalt. Wir möchte einen Ausschnitt auf der Vorderseite durch den man den Inhalt erkennen kann. Bei den Farben bitte an die des Logos halten. Grundfarbe der Verpackung kann frei gewählt werden. Beispiel der Verpackung siehe jpg. Maße (BXH) 9,5 cm x 18 cm

```html
<!DOCTYPE html>
<html lang="de">
<head>
<meta charset="utf-8">
<title>Velox Mobile – Premium Displayschutz Verpackung</title>
<link href="https://fonts.googleapis.com/css2?family=Didact+Gothic&family=Roboto+Condensed:wght@700&family=Questrial&display=swap" rel="stylesheet">
<style>
:root{
  --lime:#b1c800;
  --dark:#1c1c1c;
  --darker:#101010;
  --ink:#1a1a1a;
  --paper:#ffffff;
  --line:#2a2a2a;
}
*{margin:0;padding:0;box-sizing:border-box}
html,body{width:1200px;height:1200px;overflow:hidden;background:var(--paper)}
body{position:relative;font-family:"Didact Gothic",sans-serif;color:var(--ink)}

/* front panel */
.front{position:absolute;left:78px;top:117px;width:513px;height:967px;
  background:linear-gradient(180deg,#1e1e1e 0%,#262626 40%,#2b2b2b 60%,#111 100%);overflow:hidden}
.brand{position:absolute;display:flex;align-items:center;gap:10px;font-family:"Questrial",sans-serif;
  font-weight:400;letter-spacing:1px;white-space:nowrap}
.brand-mark{width:22px;height:22px;border-radius:50%;background:var(--lime)}
.front .brand{left:140px;top:62px;font-size:36px;color:var(--lime)}
.band{position:absolute;left:0;top:151px;width:100%;height:44px;background:var(--lime);
  display:flex;align-items:center;justify-content:center;font-family:"Questrial",sans-serif;
  font-size:27px;letter-spacing:12px;color:var(--darker);padding-left:12px}
.headline{position:absolute;left:0;top:205px;width:100%;text-align:center;color:#fff;
  font-family:"Questrial",sans-serif;font-size:62px;letter-spacing:-1px}
.product-photo{position:absolute;left:50px;top:275px;width:470px;height:640px;
  background:radial-gradient(ellipse at 60% 50%,#5a5a5a 0%,#3a3a3a 45%,#222 80%,transparent 100%)}
.features{position:absolute;left:120px;top:868px;display:flex;gap:12px}
.feature{width:46px;display:flex;flex-direction:column;align-items:center;
  font-family:"Roboto Condensed",sans-serif;font-size:10px;color:#fff;text-align:center;line-height:11px}
.feature svg{width:28px;height:28px;margin-bottom:6px}
.feature span{white-space:nowrap}

/* back panel */
.back{position:absolute;left:609px;top:117px;width:511px;height:968px;border:1px solid var(--line);background:var(--paper)}
.back .brand{left:104px;top:75px;font-size:32px;color:var(--ink)}
.copy{position:absolute;left:103px;font-size:17px;line-height:24.7px;width:360px}
.copy strong{font-family:"Roboto Condensed",sans-serif;font-weight:700;font-size:16.5px}
.intro{top:139px}
.specs{top:311px}
.install{top:385px;width:370px}
.steps{list-style:none}
.steps li{display:flex}
.steps b{font-family:"Roboto Condensed",sans-serif;width:24px;flex:none}
.delivery{top:756px}
.web{top:855px}
.step-icon{position:absolute;left:52px;width:28px}
</style>
</head>
<body>

<section class="front">
  <div class="brand"><span class="brand-mark"></span>VELOX MOBILE</div>
  <div class="band">PREMIUM</div>
  <h1 class="headline">DISPLAYSCHUTZ</h1>
  <div class="product-photo" role="img" aria-label="Foto: Hand hält ein Smartphone mit darüber schwebendem Schutzglas"></div>
  <div class="features">
    <div class="feature">
      <svg viewBox="0 0 28 28" fill="none" stroke="#fff" stroke-width="1.6"><rect x="2" y="2" width="24" height="24" rx="3"/><path d="M8 8l12 12M20 8L8 20M14 6v5"/></svg>
      <span>Bruch &amp;<br>Kratzerschutz</span>
    </div>
    <div class="feature">
      <svg viewBox="0 0 28 28" fill="none" stroke="#fff" stroke-width="1.6"><rect x="2" y="2" width="24" height="24" rx="3"/><path d="M8 20l5-12M12 20l5-12M16 20l5-12"/></svg>
      <span>Kratzfest</span>
    </div>
    <div class="feature">
      <svg viewBox="0 0 28 28" fill="none" stroke="#fff" stroke-width="1.6"><rect x="2" y="2" width="24" height="24" rx="3"/><path d="M6 14q8-8 16 0q-8 8-16 0z"/><circle cx="14" cy="14" r="2.5"/></svg>
      <span>Unsichtbar</span>
    </div>
    <div class="feature">
      <svg viewBox="0 0 28 28" fill="none" stroke="#fff" stroke-width="1.6"><rect x="2" y="2" width="24" height="24" rx="3"/><path d="M10 13q-3 4 0 6q3-2 0-6zM18 9q-3 4 0 6q3-2 0-6zM17 17q-3 4 0 5q3-1 0-5z"/></svg>
      <span>Schutz vor<br>Spritzwasser</span>
    </div>
  </div>
</section>

<section class="back">
  <div class="brand"><span class="brand-mark"></span>VELOX MOBILE</div>

  <p class="copy intro">Durch die tPassgenauigkeit und Klarheit des Premium Glasschutzes wird die Berührungsempfindlichkeit deines Smartphones nicht beeinträchtigt. Das Glas schützt dein Smartphone bei Stürzen, Stößen oder vor Kratzern durch seine extreme Härte.</p>

  <p class="copy specs"><strong>9H Härtegrad, 2.5 D abgerundete Kanten,<br>rückstandslos entfernbar</strong></p>

  <div class="copy install">
    <strong>Kurzanleitung Installation:</strong>
    <ol class="steps">
      <li><b>1</b><span>Reinige dein Display gründlich.<br>(Tücher befinden sich in der Packung)</span></li>
      <li><b>2</b><span>Entferne Staub mit dem beigefügten Aufkleber</span></li>
      <li><b>3</b><span>Nun die Folie vom Displayschutz vorsichtig entfernen und dabei jeglichen Kontakt zur Unterseite vermeiden</span></li>
      <li><b>4</b><span>Richte den Displayschutz auf deinem Smartphone aus.</span></li>
      <li><b>5</b><span>Drücke nun den Displayschutz in der Mitte an dein Smartphone. Premium Displayschutz fixiert sich automatisch.</span></li>
      <li><b>6</b><span>Entferne mit der beigefügten Rakel kleine Blasen.</span></li>
    </ol>
  </div>

  <svg class="step-icon" style="top:410px" viewBox="0 0 28 44" fill="none" stroke="#1a1a1a" stroke-width="1.6"><rect x="1" y="3" width="24" height="38" rx="3"/><path d="M16 10l1 3 3 1-3 1-1 3-1-3-3-1 3-1zM18 23l1 3 3 1-3 1-1 3-1-3-3-1 3-1z" fill="var(--lime)" stroke="none"/><rect x="8" y="35" width="10" height="2" fill="#1a1a1a" stroke="none"/></svg>
  <svg class="step-icon" style="top:486px" viewBox="0 0 28 44" fill="none" stroke="#1a1a1a" stroke-width="1.2"><rect x="1" y="1" width="24" height="40" rx="2"/><path d="M12 41L25 28v13z" fill="var(--lime)"/></svg>
  <svg class="step-icon" style="top:560px" viewBox="0 0 28 44"><rect x="1" y="1" width="26" height="42" rx="3" fill="none" stroke="#1a1a1a" stroke-width="1.8"/><rect x="5" y="5" width="20" height="32" fill="var(--lime)"/><rect x="9" y="33" width="10" height="2" fill="#1a1a1a"/></svg>
  <svg class="step-icon" style="top:612px" viewBox="0 0 28 44"><rect x="1" y="1" width="26" height="42" rx="3" fill="var(--lime)" stroke="#1a1a1a" stroke-width="1.8"/><circle cx="14" cy="20" r="7" fill="none" stroke="#fff" stroke-width="1.6"/><circle cx="14" cy="20" r="4" fill="#fff"/><rect x="9" y="36" width="10" height="2" fill="#1a1a1a"/></svg>
  <svg class="step-icon" style="top:682px" viewBox="0 0 28 44"><rect x="1" y="1" width="26" height="42" rx="3" fill="var(--lime)" stroke="#1a1a1a" stroke-width="1.8"/><circle cx="10" cy="9" r="2.5" fill="#fff"/><circle cx="18" cy="8" r="2" fill="#fff"/><path d="M6 26l14-6 4 8-14 6z" fill="#fff" stroke="#1a1a1a" stroke-width="1.2"/><rect x="9" y="37" width="10" height="2" fill="#1a1a1a"/></svg>

  <p class="copy delivery"><strong>Lieferumfang:</strong><br>Premium Displayschutz, Reinigungstuch,<br>Trockentuch, Staubsammelaufkleber, Rakel</p>

  <p class="copy web"><strong>www.veloxmobile.de</strong></p>
</section>

</body>
</html>
```